Personal Development company in need for a fun website

KV7 effectively encourages personal growth and self-improvement by providing the positive tools which will motivate, enlighten and empower the client in a relaxed, friendly environment. Taking care of the ‘self’ is essential to being productive and valuable in all aspects of life, professionally and personally. We want it to be edgy and fun targeting professionals, youth and women entering the workforce.

We would need a homepage that would have a news and features, an online shop for some of our products, a schedule for our events and workshops, a calendar, an about us section and team. Other features that need to be added terms and conditions, privacy, link to social media on the bottom of the home page.

Please look at brain dock and the hall of dawns to understand our concept.

Target Market(s)

Young professionals, women that want to enter the workplace, individuals of all ages seeking personal development in all its forms.

Industry/Entity Type

It Company

Coding

Coded - Design and coding required

Number of Pages Required

5+ page

Font styles to use
Sans Serif

Requirements
Must have
• Must be clean and attractive.
Nice to have
• Graphic design work
Should not have
• Photographs, unless its the speaker of an event.

```html
<!DOCTYPE html>
<html lang="en">
<head>
<meta charset="utf-8">
<title>KV7 — Personal Growth and Self-Improvement</title>
<link href="https://fonts.googleapis.com/css2?family=Karla:wght@400;500;700&family=PT+Sans:wght@400;700&display=swap" rel="stylesheet">
<style>
:root{
  --orange:#e4600f;
  --orange-dark:#c94a08;
  --crimson:#b5123a;
  --red-band:#c0203f;
  --ink:#222;
  --muted:#8a8a8a;
  --line:#e2e2e2;
  --card:#efefef;
  --black:#0d0d0d;
  --white:#fff;
}
*{box-sizing:border-box;margin:0;padding:0}
html,body{width:1200px;height:2350px;overflow:hidden}
body{position:relative;background:var(--white);font-family:"PT Sans",sans-serif;color:var(--ink)}

/* header */
.site-header{position:absolute;left:0;top:0;width:1200px;height:125px;background:var(--white)}
.brand{position:absolute;left:110px;top:36px;display:flex;align-items:center;gap:12px}
.brand-mark{width:16px;height:16px;background:var(--orange)}
.brand-name{font-family:"Karla",sans-serif;font-weight:700;font-size:40px;line-height:44px;color:var(--orange);letter-spacing:1px}
.contact-line{position:absolute;left:740px;top:36px;font-size:13px;color:#555}
.contact-line span{color:var(--orange);font-weight:700}
.search{position:absolute;left:936px;top:26px;width:150px;height:38px;border:2px solid #ddd;font-size:11px;color:#aaa;padding:10px 12px}
.search svg{position:absolute;right:10px;top:11px}
.main-nav{position:absolute;left:436px;top:80px;display:flex;font-family:"Karla",sans-serif;font-size:12px;text-transform:uppercase;color:#333}
.main-nav a{display:block;padding:9px 18px;height:38px;color:inherit;text-decoration:none}
.main-nav a.active{background:#eee;color:var(--crimson);font-weight:700;border-bottom:3px solid var(--crimson)}

/* hero */
.hero{position:absolute;left:0;top:125px;width:1200px;height:455px;overflow:hidden}
.hero-photo{position:absolute;left:0;top:0;width:1200px;height:455px;background:radial-gradient(ellipse at 80% 40%,#7a5a4a 0%,#4a3038 45%,#2a1e2a 100%)}
.hero-panel{position:absolute;left:0;top:0}
.hero-title{position:absolute;left:110px;top:158px;font-family:"Karla",sans-serif;font-weight:500;font-size:32px;line-height:40px;color:var(--white);letter-spacing:1.5px}
.hero-sub{position:absolute;left:112px;top:245px;font-size:14.5px;line-height:26px;color:var(--white);font-weight:700}
.hero-arrows{position:absolute;left:110px;top:315px;display:flex;gap:8px}

/* welcome */
.section-title{position:absolute;left:0;width:1200px;text-align:center;font-family:"Karla",sans-serif;font-weight:400;font-size:29px;letter-spacing:1px;color:#111}
.welcome-lead{position:absolute;left:115px;top:668px;width:970px;text-align:center;font-size:14px;line-height:26px;color:var(--crimson)}
.welcome-body{position:absolute;left:110px;top:724px;width:980px;text-align:center;font-size:11.5px;line-height:26px;color:#666}
.pillar{position:absolute;top:866px;width:310px;height:237px;background:var(--card);border:1px solid #e4e4e4;text-align:center}
.pillar-icon{position:absolute;left:95px;top:-58px}
.pillar h3{margin-top:80px;font-family:"Karla",sans-serif;font-weight:500;font-size:21px;letter-spacing:.5px;color:#222}
.pillar p{margin:12px 28px 0;font-size:11.5px;line-height:27px;color:var(--muted)}

/* events */
.events{position:absolute;left:0;top:1167px;width:1200px;height:436px;background:linear-gradient(90deg,#c61f3d 0%,#b8173a 50%,#c52545 100%)}
.events .section-title{top:66px;color:var(--white)}
.event-media{position:absolute;left:113px;top:154px;width:305px;height:199px;border:3px solid #e2505c;background:linear-gradient(180deg,#d8b070 0%,#9a6a34 55%,#3a2a22 100%)}
.event-media svg{position:absolute;left:122px;top:70px}
.event-meta{position:absolute;left:459px;top:158px;font-family:"Karla",sans-serif;font-weight:700;font-size:16px;color:var(--white);display:flex;gap:18px;align-items:center}
.event-meta span{display:flex;gap:7px;align-items:center}
.event-heading{position:absolute;left:459px;top:200px;font-size:17px;color:var(--white)}
.event-text{position:absolute;left:459px;top:240px;width:590px;font-size:11.5px;line-height:30px;color:#f8dfe3}
.slider-arrow{position:absolute;top:233px}

/* news */
.news .section-title{top:1665px}
.news-card{position:absolute;top:1730px;width:226px}
.news-thumb{width:226px;height:142px}
.news-rule{position:relative;height:2px;background:var(--orange)}
.news-rule::before,.news-rule::after{content:"";position:absolute;top:-3px;width:8px;height:8px;border-radius:50%;background:var(--orange)}
.news-rule::before{left:-2px}.news-rule::after{right:-2px}
.news-date{position:absolute;left:91px;top:120px;width:44px;height:44px;border-radius:50%;background:var(--orange);border:2px solid var(--white);color:var(--white);text-align:center;font-family:"Karla",sans-serif;font-weight:700;font-size:10px;line-height:11px;padding-top:8px}
.news-date b{display:block;font-size:15px;line-height:17px}
.news-card h4{margin-top:26px;font-size:14px;font-weight:700;line-height:26px;color:#222;text-align:justify}
.news-card p{margin-top:6px;font-size:11.5px;line-height:25px;color:var(--muted);text-align:justify}

/* footer */
.site-footer{position:absolute;left:0;top:2071px;width:1200px;height:206px;background:var(--orange)}
.footer-col{position:absolute;top:30px;color:var(--white)}
.footer-col h5{font-family:"Karla",sans-serif;font-weight:400;font-size:15.5px;letter-spacing:.5px;margin-bottom:12px}
.footer-col ul{list-style:none;font-size:11.5px;line-height:26px}
.footer-col li{display:flex;gap:8px;align-items:flex-start}
.footer-divider{position:absolute;top:30px;width:1px;height:150px;background:#f08a48}
.social-dot{width:10px;height:10px;margin-top:8px;background:var(--white)}
.footer-about{font-size:11.5px;line-height:26px;color:#ffe7d2;width:290px}
.bottom-bar{position:absolute;left:0;top:2277px;width:1200px;height:73px;background:var(--black);text-align:center;font-size:11px;color:#bbb;padding-top:30px}
.bottom-bar a{color:var(--orange);text-decoration:none;margin-left:10px}
</style>
</head>
<body>

<header class="site-header">
  <div class="brand">
    <div class="brand-mark"></div>
    <div class="brand-name">KV7</div>
  </div>
  <div class="contact-line">Get In Touch : <span>(800)555-0142</span></div>
  <div class="search">Search...
    <svg width="12" height="12" viewBox="0 0 12 12"><circle cx="5" cy="5" r="3.8" fill="none" stroke="#999" stroke-width="1.5"/><line x1="8" y1="8" x2="11" y2="11" stroke="#999" stroke-width="1.5"/></svg>
  </div>
  <nav class="main-nav">
    <a class="active">Home</a><a>News</a><a>Shop</a><a>Events &amp; Workshop</a><a>Calendar</a><a>About Us</a><a>Contact Us</a>
  </nav>
</header>

<section class="hero">
  <div class="hero-photo" role="img" aria-label="Speaker's microphone in front of a large seated audience"></div>
  <svg class="hero-panel" width="620" height="455" viewBox="0 0 620 455">
    <polygon points="0,0 590,0 545,210 590,455 0,455" fill="#a8152e"/>
    <polygon points="0,0 572,0 528,210 572,455 0,455" fill="#e4600f"/>
  </svg>
  <h1 class="hero-title">PERSONAL GROWTH<br>AND SELF-IMPROVEMENT</h1>
  <p class="hero-sub">Lorem ipsum dolor sit amet, consectetur adipiscing elit.<br>Praesent interdum facilisis convallis.</p>
  <div class="hero-arrows">
    <svg width="24" height="24" viewBox="0 0 24 24"><circle cx="12" cy="12" r="11" fill="#fff"/><path d="M14 7l-5 5 5 5" stroke="#e4600f" stroke-width="2.5" fill="none"/></svg>
    <svg width="24" height="24" viewBox="0 0 24 24"><circle cx="12" cy="12" r="11" fill="#fff"/><path d="M10 7l5 5-5 5" stroke="#e4600f" stroke-width="2.5" fill="none"/></svg>
  </div>
</section>

<section class="welcome">
  <h2 class="section-title" style="top:618px">WELCOME TO KV7</h2>
  <p class="welcome-lead">KV7 effectively encourages personal growth and self-improvement by providing the positive tools which will motivate, enlighten and empower the client in a relaxed, friendly environment.</p>
  <p class="welcome-body">Lorem ipsum dolor sit amet, consectetur adipiscing elit. Praesent ut arcu sed dolor luctus maximus sed at nunc. Duis rutrum quam eget scelerisque sollicitudin. Nulla eget convallis leo. Nunc urna velit, iaculis in nulla vel, rhoncus feugiat augue. Ut semper dolor quis nunc auctor vulputate. Integer finibus iaculis interdum. Curabitur eget ante eleifend.</p>

  <div class="pillar" style="left:111px">
    <svg class="pillar-icon" width="120" height="120" viewBox="0 0 120 120"><circle cx="60" cy="60" r="58" fill="#fff" stroke="#f2b640" stroke-width="2"/><circle cx="60" cy="60" r="50" fill="#d5560a"/><circle cx="60" cy="60" r="18" fill="none" stroke="#fff" stroke-width="4"/><circle cx="60" cy="60" r="9" fill="none" stroke="#fff" stroke-width="4"/><circle cx="60" cy="60" r="3" fill="#fff"/></svg>
    <h3>MOTIVATION</h3>
    <p>Lorem ipsum dolor sit amet, consectetur adipiscing elit. Fusce purus turpis, posuere eget libero vel, aliquam facilisis neque.</p>
  </div>
  <div class="pillar" style="left:445px">
    <svg class="pillar-icon" width="120" height="120" viewBox="0 0 120 120"><circle cx="60" cy="60" r="58" fill="#fff" stroke="#f2b640" stroke-width="2"/><circle cx="60" cy="60" r="50" fill="#d5560a"/><polygon points="64,38 50,63 59,63 54,84 70,56 61,56 68,38" fill="#fff"/></svg>
    <h3>ENLIGHTENMENT</h3>
    <p>Sed semper enim a nulla euismod, cursus facilisis turpis tincidunt. Nullam eros neque, tincidunt vitae pellentesque sed, sollicitudin.</p>
  </div>
  <div class="pillar" style="left:779px">
    <svg class="pillar-icon" width="120" height="120" viewBox="0 0 120 120"><circle cx="60" cy="60" r="58" fill="#fff" stroke="#f2b640" stroke-width="2"/><circle cx="60" cy="60" r="50" fill="#d5560a"/><rect x="40" y="56" width="8" height="22" fill="#fff"/><path d="M51 56 L58 42 Q62 38 64 44 L62 54 L76 54 Q80 55 79 59 L76 74 Q75 78 71 78 L51 78 Z" fill="#fff"/></svg>
    <h3>EMPOWERMENT</h3>
    <p>Aenean sit amet vulputate massa, in pretium orci. Morbi imperdiet lacus a ipsum porttitor euismod. Proin vitae scelerisque felis.</p>
  </div>
</section>

<section class="events">
  <h2 class="section-title">LATEST EVENTS</h2>
  <svg class="slider-arrow" style="left:56px" width="14" height="20" viewBox="0 0 14 20"><path d="M11 2L3 10l8 8" stroke="#fff" stroke-width="3" fill="none"/></svg>
  <svg class="slider-arrow" style="left:1124px" width="14" height="20" viewBox="0 0 14 20"><path d="M3 2l8 8-8 8" stroke="#fff" stroke-width="3" fill="none"/></svg>
  <div class="event-media" role="img" aria-label="Video still of an ornate hall set with rows of chairs">
    <svg width="56" height="56" viewBox="0 0 56 56"><circle cx="28" cy="28" r="25" fill="rgba(0,0,0,.25)" stroke="#fff" stroke-width="3"/><polygon points="22,16 40,28 22,40" fill="#fff"/></svg>
  </div>
  <div class="event-meta">
    <span><svg width="14" height="14" viewBox="0 0 14 14"><rect x="1" y="2" width="12" height="11" fill="none" stroke="#fff" stroke-width="1.6"/><line x1="1" y1="5.5" x2="13" y2="5.5" stroke="#fff" stroke-width="1.6"/><line x1="4" y1="0" x2="4" y2="3" stroke="#fff" stroke-width="1.6"/><line x1="10" y1="0" x2="10" y2="3" stroke="#fff" stroke-width="1.6"/></svg>JAN 20 2016</span>
    <span><svg width="11" height="15" viewBox="0 0 11 15"><path d="M5.5 0C2.5 0 0 2.4 0 5.4 0 9.5 5.5 15 5.5 15S11 9.5 11 5.4C11 2.4 8.5 0 5.5 0z" fill="#fff"/><circle cx="5.5" cy="5.4" r="2" fill="#b8173a"/></svg>LOCATION NAME</span>
  </div>
  <p class="event-heading">Lorem ipsum dolor sit amet, consectetur adipiscing elit. Praesent interdum</p>
  <p class="event-text">Etiam turpis velit, bibendum malesuada hendrerit ac, condimentum at neque. Sed semper enim a nulla euismod, cursus facilisis turpis tincidunt. Nullam eros neque, tincidunt vitae pellentesque sed, sollicitudin vel tellus. Aenean sit amet vulputate massa, in pretium orci. Morbi imperdiet lacus a ipsum porttitor euismod. Proin vitae scelerisque felis. Cras nisi ligula, dictum ut tortor et, tempor cursus ipsum.</p>
</section>

<section class="news">
  <h2 class="section-title">NEWS &amp; FEATURES</h2>
  <article class="news-card" style="left:111px">
    <div class="news-thumb" role="img" aria-label="Paper plane launched against a golden sunset sky" style="background:linear-gradient(180deg,#d9a066,#b8703a 70%,#8a4a22)"></div>
    <div class="news-rule"></div><div class="news-date">JAN<b>22</b></div>
    <h4>Aenean sit amet vulputate massa, in pretium orci.</h4>
    <p>Mauris tristique vestibulum quam, eget facilisis purus tristique in. Aenean elementum massa id lacus.</p>
  </article>
  <article class="news-card" style="left:362px">
    <div class="news-thumb" role="img" aria-label="Hand holding a pen over a tablet on a desk" style="background:linear-gradient(160deg,#e0e4ea,#9aa4b0 60%,#5a6470)"></div>
    <div class="news-rule"></div><div class="news-date">JAN<b>21</b></div>
    <h4>Sed semper enim a nulla euismod, cursus facilisis turpis</h4>
    <p>Mauris tristique vestibulum quam, eget facilisis purus tristique in. Aenean elementum massa id lacus.</p>
  </article>
  <article class="news-card" style="left:613px">
    <div class="news-thumb" role="img" aria-label="Desk lamp lighting a framed motivational sign beside a red mug" style="background:linear-gradient(180deg,#3a3a3a,#6a6058 60%,#8a3020)"></div>
    <div class="news-rule"></div><div class="news-date">JAN<b>20</b></div>
    <h4>Morbi imperdiet lacus a ipsum porttitor euismod.</h4>
    <p>Mauris tristique vestibulum quam, eget facilisis purus tristique in. Aenean elementum massa id lacus.</p>
  </article>
  <article class="news-card" style="left:863px">
    <div class="news-thumb" role="img" aria-label="Chalkboard with light bulb sketches and a ladder" style="background:linear-gradient(180deg,#2e6a3a,#1e4a28)"></div>
    <div class="news-rule"></div><div class="news-date">JAN<b>19</b></div>
    <h4>Proin vitae scelerisque felis. Cras nisi ligula, dictum ut tortor</h4>
    <p>Mauris tristique vestibulum quam, eget facilisis purus tristique in. Aenean elementum massa id lacus.</p>
  </article>
</section>

<footer class="site-footer">
  <div class="footer-col" style="left:118px">
    <h5>CONTACT US</h5>
    <ul>
      <li><svg width="10" height="13" viewBox="0 0 11 15" style="margin-top:6px"><path d="M5.5 0C2.5 0 0 2.4 0 5.4 0 9.5 5.5 15 5.5 15S11 9.5 11 5.4C11 2.4 8.5 0 5.5 0z" fill="#fff"/></svg><span style="line-height:20px;margin-top:3px">KV7<br>155 lorem ipsm, Lorem Ipsm<br>Lorem Ipsm 4227</span></li>
      <li style="margin-top:4px"><svg width="14" height="11" viewBox="0 0 14 11" style="margin-top:8px"><rect width="14" height="11" fill="#fff"/><path d="M0 0l7 6 7-6" stroke="#e4600f" fill="none"/></svg>hello@kv7mail.net</li>
      <li style="margin-top:6px"><svg width="13" height="13" viewBox="0 0 13 13" style="margin-top:7px"><path d="M3 0l2 3-1.5 1.5q1.5 3 4.5 4.5L9.5 7.5l3 2-1 2.5Q8 13 4 9T1 1z" fill="#fff"/></svg>1300 555 0198</li>
    </ul>
  </div>
  <div class="footer-divider" style="left:346px"></div>
  <div class="footer-col" style="left:392px">
    <h5>QUICK LINKS</h5>
    <ul><li>Shop</li><li>Events &amp; Workshop</li><li>Calendar</li><li>About us</li><li>Contact us</li></ul>
  </div>
  <div class="footer-divider" style="left:542px"></div>
  <div class="footer-col" style="left:578px">
    <h5>SOCIAL NETWORKS</h5>
    <ul><li><i class="social-dot"></i>Facelane</li><li><i class="social-dot"></i>Chirper</li><li><i class="social-dot"></i>RSS</li><li><i class="social-dot"></i>Orbit +</li></ul>
  </div>
  <div class="footer-divider" style="left:774px"></div>
  <div class="footer-col" style="left:807px">
    <h5>ABOUT US</h5>
    <p class="footer-about">Etiam turpis velit, bibendum malesuada hendrerit ac, condimentum at neque. Sed semper enim a nulla euis mod, cursus facilisis turpis tincidunt. Nullam eros neque, tincidunt vitae pellentesque sed,.</p>
  </div>
</footer>
<div class="bottom-bar">Copyright © 2016 KV7. All Rights Reserved. <a>Privacy Policy</a><a>Terms of Service</a></div>

</body>
</html>
```